Brindle's Coating & Renewal Letterhead Design We want to revamp out old traditional letterhead with the new logo designs that are attached. We are working on getting all our company items from vehicles, business, cards, t-shirts, letterhead to match. This should include company colors, fonts, and flow of items that we have attached below.

Industry/Entity Type

Construction Company

Font styles to use
Sans Serif
Other font styles liked:
• Bold with outline

Colors
ec1f27
ffffff

Requirements
Must have
• Company Name: Brindle's Coating & Renewal
• Address: 4172 SW 83rd Ter Harrow Cove fl 30418
• Office Number: (555) 240-6193
• Email: brindlesrenewal@mailnest-example.com
• License Number: QRT8046392
Nice to have
• Company Colors: red, white, black, and grey

```html
<!DOCTYPE html>
<html lang="en">
<head>
<meta charset="utf-8">
<title>Brindle's Coating &amp; Renewal Letterhead</title>
<link href="https://fonts.googleapis.com/css2?family=Open+Sans:wght@400;600;800&family=Lato:wght@400&display=swap" rel="stylesheet">
<style>
  :root {
    --backdrop: #e6e6e6;
    --paper: #ffffff;
    --ink: #3c3c3c;
    --ink-dark: #1f1f1f;
    --accent: #e9441f;
    --rule-grey: #b9b9b9;
    --rule: #8a8a8a;
    --signature-tone: #d9d9d9;
  }
  html, body {
    margin: 0;
    width: 1040px;
    height: 1200px;
    overflow: hidden;
    background: var(--backdrop);
  }
  .letterhead {
    position: absolute;
    left: 70px;
    top: 20px;
    width: 900px;
    height: 1160px;
    background: var(--paper);
    box-shadow: 0 2px 10px rgba(0,0,0,0.15);
    font-family: "Open Sans", sans-serif;
    color: var(--ink);
  }
  .top-band {
    position: absolute; left: 0; top: 0; width: 100%; height: 11px;
    background: var(--rule-grey);
  }
  .brand-name {
    position: absolute; left: 0; right: 0; top: 44px;
    text-align: center;
    font-weight: 800;
    font-size: 26px;
    letter-spacing: 0.5px;
    color: var(--accent);
  }
  .block {
    position: absolute; left: 84px; right: 88px;
    font-size: 14.5px;
  }
  .issue-date { top: 205px; }
  .recipient { top: 240px; line-height: 17px; }
  .salutation { top: 340px; }
  .body-copy p {
    margin: 0;
    line-height: 26px;
    text-align: justify;
    hyphens: auto;
  }
  .para-1 { top: 390px; }
  .para-2 { top: 546px; }
  .para-3 { top: 650px; }
  .closing { top: 782px; }
  .signature {
    position: absolute; left: 84px; top: 818px;
    width: 210px; height: 26px;
    background: linear-gradient(90deg, var(--signature-tone), #efefef);
    border-radius: 4px;
  }
  .signer-name { top: 856px; font-size: 18px; font-weight: 600; color: var(--ink-dark); }
  .signer-title { top: 888px; }
  .contact-line {
    position: absolute; left: 0; right: 0; top: 1088px;
    text-align: center;
    font-family: "Lato", sans-serif;
    font-size: 17px;
    color: var(--ink-dark);
  }
  .contact-line .label { color: var(--accent); }
  .footer-rule {
    position: absolute; left: 126px; right: 126px; top: 1112px;
    height: 1px; background: var(--rule);
  }
  .address-line { top: 1116px; }
  .bottom-band {
    position: absolute; left: 0; bottom: 0; width: 100%; height: 11px;
    background: var(--accent);
  }
</style>
</head>
<body>
  <main class="letterhead">
    <div class="top-band"></div>
    <div class="brand-name">Brindle's Coating &amp; Renewal</div>

    <div class="block issue-date">Issuing Date: May 5, 2018</div>
    <div class="block recipient">Name Of Employee Mr. XYZABC<br>Address of Employee<br>Address Line 2 etc..</div>
    <div class="block salutation">Dear Mr.XYZABC</div>

    <div class="block body-copy para-1"><p>Lorem Ipsum has been the industry's standard dummy text ever since the 1500s, when an unknown printer took a galley of type and scrambled it to make a type specimen book. It has survived not only five centuries, but also the leap into electronic typesetting, remaining essentially unchanged. It was popularised in the 1960s with the release of Lumaset sheets containing Lorem Ipsum passages, and more recently with desktop publishing software like Folio PageWright including versions of Lorem Ipsum.</p></div>
    <div class="block body-copy para-2"><p>Lorem Ipsum is simply dummy text of the printing and typesetting industry. Lorem Ipsum has been the industry's standard dummy text ever since the 1500s, when an unknown printer took a galley of type and scrambled it to make a type specimen book.</p></div>
    <div class="block body-copy para-3"><p>It has survived not only five centuries, but also the leap into electronic typesetting, remaining essentially unchanged. It was popularised in the 1960s with the release of Lumaset sheets containing Lorem IpsumIpsum passages.</p></div>

    <div class="block closing">Yours Sincerely</div>
    <div class="signature" role="img" aria-label="Handwritten signature of Dorian Wexley"></div>
    <div class="block signer-name">Dorian Wexley</div>
    <div class="block signer-title">Managing Director</div>

    <div class="contact-line"><span class="label">P:</span> (555) 240-6193 | <span class="label">E:</span> brindlesrenewal@mailnest-example.com | <span class="label">License Number:</span> QRT8046392</div>
    <div class="footer-rule"></div>
    <div class="contact-line address-line">BRINDLE'S COATING &amp; RENEWAL : 4172 SW 83rd Ter Harrow Cove fl 30418</div>
    <div class="bottom-band"></div>
  </main>
</body>
</html>
```